Broschüre
Zielgruppe
Firmen und Privatpersonen
Unsere Zielkunden sind im bereich Firmen
Firmen die etwas für die Umwelt tun wollen oder sich einen Grünen anstrich geben wollen
Privatpersonen hier ist es die Gruppe die sich für den erhalt der Natur einsetzten die Bienen oder Naturprojekte unterstützen wollen und dergleichen. In der regel Menschen die BIO Kaufen
Aufgabenstellung
Standard Falzflyer DIN-A4 4 Seiten / Logo vorhanden / Unbedingt noch ein Freifeld zum ausfüllen zum bestellen. Daten die wir zum bestellen benötigen Name/Adresse/Telefonnummer/E-Mail/Unterschrift

```html
<!DOCTYPE html>
<html lang="de">
<head>
<meta charset="utf-8">
<title>Imker auf Zeit – Broschüre</title>
<link rel="stylesheet" href="https://fonts.googleapis.com/css2?family=Crimson+Text:wght@400;600&display=swap">
<style>
  :root {
    --band: #fdd86a;
    --band-edge: #3a3a3a;
    --paper: #ffffff;
    --ink: #1c1c1c;
    --photo-honey: #c9a55a;
    --photo-green: #8fa86a;
    --photo-sky: #7fb6e6;
    --photo-meadow: #9ec46a;
  }
  * { margin: 0; padding: 0; box-sizing: border-box; }
  html, body { width: 1200px; height: 741px; overflow: hidden; background: var(--paper); }
  body {
    position: relative;
    font-family: "Crimson Text", Georgia, serif;
    color: var(--ink);
    font-size: 14.5px;
    line-height: 22.5px;
  }
  .top-band {
    position: absolute; left: 0; top: 0; width: 1200px; height: 45px;
    background: var(--band);
    border: 1px solid var(--band-edge);
  }
  .block { position: absolute; text-align: justify; hyphens: auto; }
  .page-title {
    position: absolute; left: 45px; width: 450px; top: 50px;
    text-align: center; font-size: 30px; font-weight: 400; line-height: 40px;
  }
  .intro { left: 45px; top: 152px; width: 450px; }
  .photo { position: absolute; }
  .photo-child {
    left: 45px; top: 209px; width: 216px; height: 222px;
    background: linear-gradient(135deg, var(--photo-honey), #e3d9c4 55%, var(--photo-green));
  }
  .rent-text { left: 268px; top: 210px; width: 226px; text-indent: 12px; }
  .curious { left: 45px; top: 503px; width: 450px; }
  .page-no { position: absolute; top: 694px; font-size: 13px; }
  .page-no--left { left: 45px; }
  .page-no--right { left: 1100px; width: 55px; text-align: right; }
  .rescue-heading { position: absolute; left: 645px; top: 49px; font-size: 14.5px; }
  .rescue-text { left: 645px; top: 112px; width: 510px; line-height: 22px; }
  .rescue-text p:first-child { text-indent: 12px; }
  .photo-beekeepers {
    left: 645px; top: 401px; width: 510px; height: 294px;
    background: linear-gradient(180deg, var(--photo-sky) 0%, #b9d6ee 30%, var(--photo-meadow) 55%, #e9e4d6 100%);
  }
</style>
</head>
<body>
  <div class="top-band"></div>

  <h1 class="page-title">Imker auf Zeit</h1>
  <p class="block intro">Werde Imker auf Zeit und miete deinen eigenen Bienenstock voller fleißiger Bestäuber.</p>
  <div class="photo photo-child" role="img" aria-label="Kind in Imkeranzug mit Schleierhut und Smoker vor Bienenstöcken"></div>
  <p class="block rent-text">Wollten Sie schon immer Imker werden und eigenen Honig haben? Jetzt gibt es die Möglichkeit in die Imkerei hinein zu schnuppern und einen Bienenstock für zwei Monate (190 Euro) oder eine Saison (290 Euro) zu „mieten“. Nach dieser Zeit gibt es den fix fertig abgefüllten Honig „ihrer“ Bienen in 1-Kilo-Gläsern. „Alles was das Bienenvolk im Honigraum sammelt gehört Ihnen“, und kann an Ihre Liebsten und Freunde verschenkt werden.</p>
  <p class="block curious">Wer einen Blick in das faszinierende Treiben seines Bienenvolk werfen möchte, hat die Möglichkeit ein „Neugier-Paket“ dazu zu nehmen, welches eine Imkerjacke, einen Smoker und Handschuhe beinhaltet. „Damit kann man jederzeit nachschauen, was die Bienen so treiben. Natürlich gibt es auch eine Einschulung bei „Abholung“.</p>
  <span class="page-no page-no--left">S. 3</span>

  <h2 class="rescue-heading">Bienenretter werden - leicht gemacht!</h2>
  <div class="block rescue-text">
    <p>Mit den „Bienen auf Zeit“ kann man die Rolle des Beobachters gegen die des Machers tauschen. „So kann man das Bienenvolk beobachten, begleiten und betreibt auch noch aktiven Naturschutz. „Man muss nur darauf achten den Bienenstock an einem nicht zu windigen Platz aufzustellen“, und richtig auszurichten.</p>
    <p>Aber auch zuhause im Garten kann man einiges für die Bienen tun. Es ist oft leichter als man glaubt, den kleinen Bienen zu helfen in dem man Blumen und Sträucher setzt, die alle Bestäuber lieben. Dazu gehören zum Beispiel Schneeglöckchen, Krokus, Lavendel oder Bohnenkraut um nur einige zu nennen. Blütenhof führt ein breites Sortiment an Pflanzen, die unsere Bienen lieben.</p>
    <p>„Gemeinschaftlich können wir zeigen, was nötig und möglich ist, um Österreich wieder bienenfreundlicher zu machen. Helfen Sie mit, den Bienen vielfältige und abwechslungsreiche Lebensräume bereitzustellen und deren Überleben zu sichern.</p>
  </div>
  <div class="photo photo-beekeepers" role="img" aria-label="Zwei Imker mit Schleierhüten halten Bienenwaben vor bunten Bienenstöcken auf einer Wiese"></div>
  <span class="page-no page-no--right">S. 4</span>
</body>
</html>
```